We are looking to launch a website related to “cuesports”, especially snooker. Snooker is a popular sport in The UK and worldwide.

We are looking to build 2 pages with you for this contest

- the homepage
- and a page which will be used FOR EACH player we are working with and promoting (More below)

At the moment we have no idea about the design but it should be classy, ie. maybe similar to many of the high end fashion sites - maybe this kind of look?

https://www.plorvex.co.uk/search?q=high+end+websites&espv=2&biw=1396&bih=694&source=lnms&tbm=isch&sa=X&ved=0ahUKEwiq6MaprYvPAhVoKcAKHW8mCiUQ_AUIBigB#tbm=isch&q=classy+websites

UNLESS THIS IS COMPLETELY THE WRONG IDEA FOR WHAT WE ARE DOING, we will leave it up to you to show us some of your best ideas and help us succeed!

We are more interested in the layout and design than the text at this stage. We can add gthe main text later with your help or by ourselves, but Design, look and feel is what we want to see for this contes. Obviously if you have any questions we will give you regular feedback during the time of this contest.

This will be an ecommerce site but we expect to get to the shopping cart stage in about a month

Our main marketing tool will be our website.

There are 3 core parts to our business in priority order:

1. Sales of Snooker/Billiards Equipment
We will be selling everything from the smallest items, snooker tips, chalk, to snooker cues (sticks) all the way to Major items such as snooker tables.

Here are some typical sites that sell snooker related equipment:

http://www.mikedelwinbaizegear.com/
http://www.feltorvium.co.uk/
http://www.qrtpockets.co.uk/

2. Sale of our own branded fashion accessories: T’shirts, Caps, jackets, cologne etc etc

3. Our booking section, where we will promote famous snooker players and other sports stars for exhibitions, after dinner speaking, golf days, etc
(probably 1 page per player in the booking section with a picture, brief bio, summary of the kind of things they can be booked for and perhaps a tarrif sheet, though we may not publish this information online and prefer to ask people to contact us if they wish to book a player

Target Markets

Mainly the UK and Europe, but snooker is becoming increasingly popular in China

Demographics are mostly males aged 16 and 40

Logo Design (separate contest at a later time)

1. The design must project a sense of professionalism and have a high class feel

2. Must Have Priorities:

- Modern, professional and friendly.
- Strong emphasis on usability.
- mobile friendly - responsive

3. Should not Have:

- An anonymous cold and corporate feel.
- A too busy feel.

4. The winner of this design contest will also be awarded a freelance project to help us further develop/complete the site.

Thank You everyone and Good luck !

Target Market(s)

18-40 mainly

Number of Pages Required

2 page

Requirements
Must have
• - Modern, professional and friendly.
• - Strong emphasis on usability.
• - mobile friendly - responsive
Should not have
• - An anonymous cold and corporate feel.
• - A too busy feel.

```html
<!DOCTYPE html>
<html lang="en">
<head>
<meta charset="utf-8">
<title>Cue Shop – Home</title>
<link rel="stylesheet" href="https://fonts.googleapis.com/css2?family=Montserrat:wght@700;800;900&family=Mulish:wght@400;600;700;800&display=swap">
<style>
:root{
  --red:#f04a4c;
  --white:#ffffff;
  --ink:#111111;
  --dark:#232323;
  --black:#0b0b0b;
}
*{box-sizing:border-box;margin:0;padding:0}
html,body{width:1200px;height:3879px;overflow:hidden}
body{position:relative;background:var(--white);font-family:"Mulish",Arial,sans-serif;color:var(--white)}
.abs{position:absolute}
.head{font-family:"Montserrat",Arial,sans-serif;font-weight:900;text-transform:uppercase}

.hero-bg{position:absolute;left:0;top:0;width:1200px;height:1870px}
.menu{left:31px;top:21px;width:47px;height:34px}
.shop-icon{top:22px;width:56px;text-align:center;font-size:13px;color:var(--ink)}
.shop-icon svg{display:block;margin:0 auto 4px}

.photo{position:absolute}
.tile-eight{left:246px;top:0;width:235px;height:478px;
  background:radial-gradient(ellipse 75% 45% at 45% 38%,#8a8a8a 0%,#4a4a4a 35%,#1c1c1c 70%,#0c0c0c 100%)}
.tile-table{left:481px;top:0;width:476px;height:238px;
  background:radial-gradient(ellipse 90% 85% at 62% 30%,#f4f4f4 0%,#d2d2d2 35%,#8c8c8c 70%,#3c3c3c 100%)}
.tile-cues{left:481px;top:238px;width:476px;height:476px;
  background:linear-gradient(145deg,#2a2a2a 0%,#4e4e4e 30%,#a8a8a8 48%,#5a5a5a 58%,#262626 78%,#141414 100%)}
.hero-logo{left:483px;top:238px;width:234px;height:238px;background:var(--red);display:flex;align-items:center;justify-content:center;font-family:"Montserrat",Arial,sans-serif;font-weight:800;font-size:52px;color:var(--white)}
.slogan{font-size:58px;line-height:75px;color:var(--white)}
.hero-text{left:200px;top:768px;width:812px;text-align:center;font-weight:800;font-size:24.5px;line-height:41px}

.section-title{left:0;width:1200px;text-align:center;font-size:44px;letter-spacing:1px}
.cat{position:absolute;top:1076px;width:212px;height:382px}
.cat-label{position:absolute;left:0;right:0;top:210px;text-align:center;font-family:"Montserrat",Arial,sans-serif;font-weight:800;font-size:24px;line-height:34px;text-transform:uppercase}
.cat-btn{position:absolute;left:50%;top:294px;transform:translateX(-50%);width:118px;height:28px;border:2px solid var(--white);font-size:12px;font-weight:700;display:flex;align-items:center;justify-content:center}

.winner{left:16px;top:1515px;width:1166px;height:541px;
  background:linear-gradient(158deg,#1e1e1e 0%,#5a5a5a 22%,#2a2a2a 40%,#444 55%,#9a9a9a 72%,#3a3a3a 86%,#161616 100%)}
.winner-title{left:86px;top:1577px;font-size:54px;line-height:76px}
.winner-text{left:140px;top:1840px;width:840px;text-align:center;font-weight:800;font-size:25px;line-height:36px}

.community{left:0;top:2141px;width:1200px;height:1324px;background:var(--dark)}
.community-title{left:0;top:2236px;width:1200px;text-align:center;font-family:"Montserrat",Arial,sans-serif;font-weight:800;font-size:58px;color:var(--red)}
.player-photo{position:absolute}
.photo-caption{position:absolute;text-align:right;font-family:"Montserrat",Arial,sans-serif;font-weight:800;color:var(--white);white-space:nowrap}
.rule{position:absolute;width:6px;background:var(--white)}
.story{position:absolute;font-size:16.5px;line-height:22.5px;text-align:justify;color:var(--white)}
.btn-outline{position:absolute;border:2px solid var(--white);display:flex;align-items:center;justify-content:center;font-size:19px}

.subscribe{left:0;top:3465px;width:1200px;height:130px;background:var(--red)}
.subscribe-title{left:0;top:3494px;width:1200px;text-align:center;font-size:28px}
.sub-input{left:372px;top:3550px;width:329px;height:24px;background:var(--white);border-radius:12px}
.sub-btn{left:724px;top:3550px;width:140px;height:25px;background:var(--ink);border-radius:12px;font-size:13px;font-weight:700;display:flex;align-items:center;justify-content:center}

.footer{left:0;top:3595px;width:1200px;height:284px;background:var(--black)}
.foot-list{list-style:none;font-size:19px;line-height:42px}
.foot-logo{left:527px;top:3693px;width:187px;height:85px;border:3px solid var(--white);display:flex;align-items:center;justify-content:center;font-family:"Montserrat",Arial,sans-serif;font-weight:800;font-size:42px}
.foot-text{font-size:19px;line-height:28px}
.copyright{left:0;top:3841px;width:1200px;text-align:center;font-size:18px}
</style>
</head>
<body>

<!-- Hero -->
<svg class="hero-bg" viewBox="0 0 1200 1870" aria-hidden="true"><polygon points="0,0 1200,0 1200,1605 0,1862" fill="var(--red)"/></svg>

<svg class="abs menu" viewBox="0 0 47 34" aria-label="Menu"><rect width="47" height="6" fill="#111"/><rect y="14" width="47" height="6" fill="#111"/><rect y="28" width="47" height="6" fill="#111"/></svg>

<div class="abs shop-icon" style="left:1016px">
  <svg width="46" height="40" viewBox="0 0 46 40" aria-hidden="true"><path d="M2 4h8l6 22h22l5-16H13" fill="none" stroke="#111" stroke-width="3.5" stroke-linejoin="round"/><circle cx="19" cy="34" r="3.5" fill="#111"/><circle cx="35" cy="34" r="3.5" fill="#111"/></svg>
  Cart
</div>
<div class="abs shop-icon" style="left:1117px">
  <svg width="44" height="44" viewBox="0 0 44 44" aria-hidden="true"><circle cx="22" cy="22" r="18" fill="none" stroke="#111" stroke-width="3.5" stroke-dasharray="6 3"/><circle cx="16" cy="16" r="3" fill="#111"/><circle cx="28" cy="28" r="3" fill="#111"/><line x1="29" y1="14" x2="15" y2="30" stroke="#111" stroke-width="3"/></svg>
  Discount
</div>

<div class="photo tile-eight" role="img" aria-label="Black eight ball resting by a cue tip, dark monochrome photo"></div>
<div class="photo tile-table" role="img" aria-label="Eight ball on a pale table, monochrome photo"></div>
<div class="photo tile-cues" role="img" aria-label="Row of cues laid diagonally, monochrome photo"></div>
<div class="abs hero-logo">logo</div>
<div class="abs head slogan" style="left:254px;top:250px">Play<br>your<br>way</div>
<div class="abs head slogan" style="left:512px;top:482px">Buy<br>your<br>way</div>

<p class="abs hero-text">Lorem ipsum dolor sit amet, consectetur adipiscing elit. Vivamus ut nunc lorem. Cras ac tincidunt nibh. Mauris aliquam diam ac justo volutpat, et consectetur est commodo. Curabitur a dui diam. Curabitur facilisis sapien ac tempor congue. Vi-</p>

<!-- Categories -->
<h2 class="abs head section-title" style="top:992px">Choose category to shop</h2>

<div class="cat" style="left:23px;background:radial-gradient(ellipse 90% 60% at 50% 20%,#8a3022 0%,#4a2a1e 40%,#1e2a20 75%,#101010 100%)" role="img" aria-label="Chalk and accessories on a table photo">
  <div class="cat-label">Accessories</div><div class="cat-btn">SHOP NOW</div>
</div>
<div class="cat" style="left:260px;background:linear-gradient(100deg,#1d5c18 0%,#3e7a22 20%,#9a7a3a 38%,#2f6a1e 52%,#8a6a30 68%,#2a7a20 85%,#1a5a14 100%)" role="img" aria-label="Cues lying on green cloth photo">
  <div class="cat-label">Cues</div><div class="cat-btn">SHOP NOW</div>
</div>
<div class="cat" style="left:497px;background:radial-gradient(ellipse 80% 70% at 50% 45%,#d0702a 0%,#9a3a2a 30%,#2e3c8a 60%,#141414 100%)" role="img" aria-label="Pile of coloured pool balls photo">
  <div class="cat-label">Balls</div><div class="cat-btn">SHOP NOW</div>
</div>
<div class="cat" style="left:734px;background:linear-gradient(155deg,#3a6ab0 0%,#6a7ab8 25%,#a4508a 50%,#7a9a6a 75%,#5a8a5a 100%)" role="img" aria-label="Table tops in many cloth colours photo">
  <div class="cat-label">Tables</div><div class="cat-btn">SHOP NOW</div>
</div>
<div class="cat" style="left:971px;background:linear-gradient(160deg,#2a2222 0%,#9a3a36 30%,#d8d0c8 48%,#7a2e2e 62%,#2a2020 100%)" role="img" aria-label="Pool cues in cue cases photo">
  <div class="cat-label" style="top:190px">Pool &amp;<br>cue cases</div><div class="cat-btn">SHOP NOW</div>
</div>

<!-- Promo banner -->
<div class="abs winner" role="img" aria-label="Crossed cues over racked balls, monochrome photo"></div>
<div class="abs head winner-title">Be<br>the<br>winner</div>
<p class="abs winner-text">Lorem ipsum dolor sit amet, consectetur adipiscing elit. Vivamus ut nunc lorem. Cras ac tincidunt nibh. Mauris aliquam diam ac justo volutpat, et consectetur est commodo. Curabitur a dui diam. Curabitur facilisis sapien ac tempor congue. Vi-</p>

<!-- Community -->
<section class="abs community" aria-label="Community"></section>
<h2 class="abs community-title">Communinty</h2>

<div class="player-photo" style="left:49px;top:2343px;width:820px;height:401px;background:radial-gradient(ellipse 60% 90% at 58% 55%,#8a7060 0%,#3a2a2a 35%,#5a1a1e 65%,#2a1216 100%)" role="img" aria-label="Player celebrating with a trophy"></div>
<div class="photo-caption" style="left:650px;top:2510px;width:202px;font-size:31px;line-height:42px">Lorem<br>ipsum<br>dolor sit<br>amet, con-</div>
<div class="rule" style="left:874px;top:2348px;height:395px"></div>
<p class="story" style="left:890px;top:2366px;width:238px">Lorem ipsum dolor sit amet, consectetur adipiscing elit. Nunc ut ligula non lorem egestas bibendum eget id est. Sed erat odio, suscipit sit amet augue sed, luctus efficitur odio. Nunc commodo turpis in felis posuere, a imperdiet urna sagittis. Curabitur tempus mi egestas mi tincidunt elementum. Donec vitae quam mauris. Curabitur eget nunc ut felis pulvinar fringilla vitae tempus purus. Praesent sollicitudin, mauris</p>

<div class="player-photo" style="left:57px;top:2770px;width:274px;height:520px;background:linear-gradient(175deg,#6a6660 0%,#2a2624 30%,#1a1a1a 50%,#3a6a3a 72%,#8a2a20 100%)" role="img" aria-label="Player in waistcoat beside a trophy"></div>
<div class="photo-caption" style="left:140px;top:2852px;width:180px;font-size:29px;line-height:40px">Lorem<br>ipsum<br>dolor sit<br>amet, con-</div>
<div class="rule" style="left:341px;top:2770px;height:250px"></div>
<p class="story" style="left:360px;top:2790px;width:286px">Lorem ipsum dolor sit amet, consectetur adipiscing elit. Nunc ut ligula non lorem egestas bibendum eget id est. Sed erat odio, suscipit sit amet augue sed, luctus efficitur odio. Nunc commodo turpis in felis posuere, a imperdiet urna sagittis. Curabitur tempus mi egestas mi tincidunt elementum. Donec vitae quam mauris. Curabitur eget nunc</p>

<div class="player-photo" style="left:690px;top:2770px;width:492px;height:266px;background:linear-gradient(180deg,#2a1e16 0%,#4a3424 30%,#2a2a22 52%,#2a8a34 68%,#1e6a26 100%)" role="img" aria-label="Player leaning over the table taking a shot"></div>

<div class="player-photo" style="left:352px;top:3044px;width:323px;height:246px;background:linear-gradient(180deg,#3a3634 0%,#5a4a40 30%,#2a3a2a 55%,#2a7a30 75%,#1a5a20 100%)" role="img" aria-label="Player lining up a shot on the table"></div>
<div class="photo-caption" style="left:480px;top:3110px;width:180px;font-size:29px;line-height:40px">Lorem<br>ipsum<br>dolor sit<br>amet, con-</div>
<div class="rule" style="left:681px;top:3051px;height:250px"></div>
<p class="story" style="left:708px;top:3090px;width:466px">Lorem ipsum dolor sit amet, consectetur adipiscing elit. Nunc ut ligula non lorem egestas bibendum eget id est. Sed erat odio, suscipit sit amet augue sed, luctus efficitur odio. Nunc commodo turpis in felis posuere, a imperdiet urna sagittis. Curabitur tempus mi egestas mi tincidunt elementum. Donec vitae quam mauris. Curabitur eget nunc ut felis pulvinar fringilla vitae tempus purus. Praesent sollicitudin, mauris id sodales fermentum, purus quam varius orci, id commodo metus sem sit amet ipsum. Etiam ut fini-</p>

<div class="btn-outline" style="left:525px;top:3362px;width:178px;height:47px">Read more</div>

<!-- Subscribe -->
<section class="abs subscribe" aria-label="Subscribe"></section>
<h3 class="abs head subscribe-title">Subscribe now for news &amp; latest offers</h3>
<div class="abs sub-input" aria-label="Email address"></div>
<div class="abs sub-btn">Subscribe now</div>

<!-- Footer -->
<footer class="abs footer"></footer>
<ul class="abs foot-list" style="left:98px;top:3633px">
  <li>Home</li><li>Site Map</li><li>Shop Now</li><li>Community</li><li>Contact us</li>
</ul>
<div class="rule" style="left:240px;top:3650px;height:150px"></div>
<ul class="abs foot-list" style="left:287px;top:3633px">
  <li>Support</li><li>Feedback us</li><li>Pinewall page</li><li>Chatterly account</li>
</ul>
<div class="abs foot-logo">Logo</div>
<p class="abs foot-text" style="left:856px;top:3683px">Follow us<br>Pinewall,<br>Chatterly</p>
<div class="rule" style="left:965px;top:3668px;height:132px"></div>
<p class="abs foot-text" style="left:1003px;top:3666px">Address:<br>Door no. 123,<br>Street name,<br>City - 123456,<br>Country.</p>
<p class="abs copyright">Copyright © 2016 Cue shop</p>

</body>
</html>
```